Logo & Business card - Want to paint the town?

Brushvane - Top Quality Painting & Decorating

Brushvane are a painting & decorating company who work predominantly in the residential market and not commercial. We require a logo and business cards design

The company is based Christchurch NZ. Christchurch had major earthquakes in 2010 and 2011, which devastated the city. The city is in rebuild and fixing phase and will be for the next 5 years to get the city back on it's feet. As a result of the earthquakes are a lot of homes being fixed that require painting and decorating.

Additional to the earthquake work there is also huge growth in the city meaning lots of new homes are being built to accommodate the growth.

Alongside this there is an every growing rental market, so we not only work on residential earthquake repairs and new builds but also work with real estate agents, property managers and interior designers.

Christchurch has seen a large number of tradesmen enter the market and not all of whom are qualified/skilled. Our company’s painters are those with years of experience and who pride themselves on top quality precision work.

Brushvane are about quality jobs, done to a very high level at an affordable price. We are not the cheapest but also not the most expensive. Our logo and cards must reflect the quality of our work. Brushvane requires a professional logo and business card targeted to the higher end of the residential market.

Target Market(s)

Builders requiring contract painters, housing companies such as Tom Halvick, Stalwart buildings, Ridgeway Home etc., real estate agents, property managers, interior designers and home owners.

The business cards and logo must appeal to builders, homeowner, interior designers and real estate agents so can’t be too masculine/feminine.

It needs to be bold, professional and stylish.

Industry/Entity Type

Residential

Logo Text

Brushvane

Logo styles of interest
Wordmark Logo
Requirements
Must have
• The logo and business cards must be bold, clean, modern, smart, simple, self explanatory, tidy, easy to read, timeless, and not frilly.

We are about quality, precision and being able to cut a straight line, so the card needs to avoid and curvy brush strokes as this denotes a bad a and sloppy painter.

The card and logo must scream top quality and affordability.
The card must be clean and modern, high end and stylish.

The logo must be something, which will go well on a silver/ black background as eventually as the van fleet will be either silver or black, so it must punch out on these colours.

For contact details that need to appear on the business cards see the full brief attached.
Nice to have
• One idea could be to have a picture on the business card of a well-painted stylish modern home interior, which would eventually be replaced by picture of Brushvane's paint jobs.
Should not have
• It definitely must not include is paint drips; paint pot with dribbles over the side of it, splurges of paint, or paintbrush swooshes as this indicates a messy painter.

Most colours are ok except for pink, orange or pastel colours.

```html
<!DOCTYPE html>
<html lang="en">
<head>
<meta charset="utf-8">
<title>Brushvane – Business Cards</title>
<link href="https://fonts.googleapis.com/css2?family=Roboto:wght@300;400;500;700&display=swap" rel="stylesheet">
<style>
  :root {
    --page-bg: #1d1a21;
    --card-bg: #050505;
    --lime: #b8cf3c;
    --white: #ffffff;
    --muted: #b5b5b5;
    --divider: #8a8a8a;
    --icon: #ffffff;
  }
  * { box-sizing: border-box; margin: 0; padding: 0; }
  html, body {
    width: 1200px; height: 1200px; overflow: hidden;
    background: var(--page-bg);
    font-family: "Roboto", Arial, sans-serif;
  }
  .sheet {
    position: absolute; left: 20px; top: 250px;
    display: grid;
    grid-template-columns: 560px 560px;
    grid-template-rows: 330px 330px;
    gap: 40px;
  }
  .card {
    position: relative; width: 560px; height: 330px;
    background: var(--card-bg); overflow: hidden;
  }
  .card--grey   { --stripe: transparent; --band-1: #8d8d8d; --band-2: #858585; --band-3: #7d7d7d; }
  .card--berry  { --stripe: #8c4f8c; --band-1: #8b4c8a; --band-2: #4fa88a; --band-3: #c98743; }
  .card--violet { --stripe: #8a7fb8; --band-1: #5e5499; --band-2: #a59fcc; --band-3: #8a80c0; }

  .card__stripe { position: absolute; left: 0; top: 0; width: 100%; height: 9px; background: var(--stripe); }

  .wordmark {
    position: absolute; white-space: nowrap;
    color: var(--white); font-weight: 500; letter-spacing: -0.5px; line-height: 1;
  }
  .card--front .wordmark { left: 50%; top: 50%; transform: translate(-50%, -50%); font-size: 84px; }
  .card--back .wordmark { left: 250px; top: 84px; font-size: 56px; }

  .holder { position: absolute; left: 40px; top: 86px; }
  .holder__name { font-size: 17px; color: var(--white); font-weight: 300; letter-spacing: 0.3px; }
  .holder__first { color: var(--lime); font-weight: 700; }
  .holder__role { margin-top: 4px; font-size: 12px; color: var(--muted); font-weight: 300; }

  .divider { position: absolute; left: 215px; top: 55px; width: 1px; height: 110px; background: var(--divider); }

  .bands { position: absolute; left: 0; top: 0; width: 560px; height: 330px; }
  .band-1 { fill: var(--band-1); }
  .band-2 { fill: var(--band-2); }
  .band-3 { fill: var(--band-3); }
  .icon { fill: none; stroke: var(--icon); stroke-width: 1.3; }
  .icon--solid { fill: var(--icon); stroke: none; }

  .contact {
    position: absolute; left: 100px; font-size: 13px; line-height: 18px;
    color: var(--white); font-weight: 400; letter-spacing: 0.2px;
  }
  .contact--phone { top: 220px; }
  .contact--email { top: 250px; }
  .contact--web   { top: 280px; }
</style>
</head>
<body>
<main class="sheet">

  <section class="card card--front">
    <div class="wordmark">Brushvane</div>
  </section>

  <section class="card card--back card--grey">
    <div class="holder">
      <p class="holder__name"><span class="holder__first">JENNA</span> CORWELL</p>
      <p class="holder__role">Designation</p>
    </div>
    <div class="divider"></div>
    <div class="wordmark">Brushvane</div>
    <svg class="bands" viewBox="0 0 560 330" aria-hidden="true">
      <rect class="band-1" x="0" y="214" width="50" height="29"/>
      <polygon class="band-1" points="84,214 560,231 560,245 84,243"/>
      <rect class="band-2" x="0" y="247" width="50" height="23"/>
      <polygon class="band-2" points="84,247 560,250 560,266 84,270"/>
      <rect class="band-3" x="0" y="276" width="50" height="26"/>
      <polygon class="band-3" points="84,276 560,268 560,284 84,302"/>
      <path class="icon--solid" d="M62 222 q2 -2 4 0 l2 3 q1 2 -1 3 q1 3 4 4 q1 -2 3 -1 l3 2 q2 2 0 4 q-2 2 -5 1 q-8 -3 -11 -11 q-1 -3 1 -5z"/>
      <rect class="icon" x="61" y="253" width="15" height="11"/>
      <polyline class="icon" points="61,253 68.5,260 76,253"/>
      <circle class="icon" cx="68.5" cy="289" r="7"/>
      <ellipse class="icon" cx="68.5" cy="289" rx="3" ry="7"/>
      <line class="icon" x1="61.5" y1="289" x2="75.5" y2="289"/>
    </svg>
    <span class="contact contact--phone">021 47 83 12</span>
    <span class="contact contact--email">info@brushvane.co.nz</span>
    <span class="contact contact--web">www.brushvane.co.nz</span>
  </section>

  <section class="card card--back card--berry">
    <div class="card__stripe"></div>
    <div class="holder">
      <p class="holder__name"><span class="holder__first">JENNA</span> CORWELL</p>
      <p class="holder__role">Designation</p>
    </div>
    <div class="divider"></div>
    <div class="wordmark">Brushvane</div>
    <svg class="bands" viewBox="0 0 560 330" aria-hidden="true">
      <rect class="band-1" x="0" y="214" width="50" height="29"/>
      <polygon class="band-1" points="84,214 560,231 560,245 84,243"/>
      <rect class="band-2" x="0" y="247" width="50" height="23"/>
      <polygon class="band-2" points="84,247 560,250 560,266 84,270"/>
      <rect class="band-3" x="0" y="276" width="50" height="26"/>
      <polygon class="band-3" points="84,276 560,268 560,284 84,302"/>
      <path class="icon--solid" d="M62 222 q2 -2 4 0 l2 3 q1 2 -1 3 q1 3 4 4 q1 -2 3 -1 l3 2 q2 2 0 4 q-2 2 -5 1 q-8 -3 -11 -11 q-1 -3 1 -5z"/>
      <rect class="icon" x="61" y="253" width="15" height="11"/>
      <polyline class="icon" points="61,253 68.5,260 76,253"/>
      <circle class="icon" cx="68.5" cy="289" r="7"/>
      <ellipse class="icon" cx="68.5" cy="289" rx="3" ry="7"/>
      <line class="icon" x1="61.5" y1="289" x2="75.5" y2="289"/>
    </svg>
    <span class="contact contact--phone">021 47 83 12</span>
    <span class="contact contact--email">info@brushvane.co.nz</span>
    <span class="contact contact--web">www.brushvane.co.nz</span>
  </section>

  <section class="card card--back card--violet">
    <div class="card__stripe"></div>
    <div class="holder">
      <p class="holder__name"><span class="holder__first">JENNA</span> CORWELL</p>
      <p class="holder__role">Designation</p>
    </div>
    <div class="divider"></div>
    <div class="wordmark">Brushvane</div>
    <svg class="bands" viewBox="0 0 560 330" aria-hidden="true">
      <rect class="band-1" x="0" y="214" width="50" height="29"/>
      <polygon class="band-1" points="84,214 560,231 560,245 84,243"/>
      <rect class="band-2" x="0" y="247" width="50" height="23"/>
      <polygon class="band-2" points="84,247 560,250 560,266 84,270"/>
      <rect class="band-3" x="0" y="276" width="50" height="26"/>
      <polygon class="band-3" points="84,276 560,268 560,284 84,302"/>
      <path class="icon--solid" d="M62 222 q2 -2 4 0 l2 3 q1 2 -1 3 q1 3 4 4 q1 -2 3 -1 l3 2 q2 2 0 4 q-2 2 -5 1 q-8 -3 -11 -11 q-1 -3 1 -5z"/>
      <rect class="icon" x="61" y="253" width="15" height="11"/>
      <polyline class="icon" points="61,253 68.5,260 76,253"/>
      <circle class="icon" cx="68.5" cy="289" r="7"/>
      <ellipse class="icon" cx="68.5" cy="289" rx="3" ry="7"/>
      <line class="icon" x1="61.5" y1="289" x2="75.5" y2="289"/>
    </svg>
    <span class="contact contact--phone">021 47 83 12</span>
    <span class="contact contact--email">info@brushvane.co.nz</span>
    <span class="contact contact--web">www.brushvane.co.nz</span>
  </section>

</main>
</body>
</html>
```